Bright Summit Web Design

I am starting a new company that will provide LIFE COACHING services - I have tried to design a website, but it's too complicated. Right now, it's just me - I'm the only person that will provide services through the website - I have used makerhive to purchase a logo (see below). I want to be able to update the website myself, but need a template - basic design. Because I am not technologically savvy enough to explain in words - I basically want to have a website that will provide basic information about my services (coaching), a page about me and my background, hopefully scheduling possibilities, and testimonials — also a page for writing/blogs. I bought a website through NetBarn - so when I have a template, I guess I”d use that - but maybe I’ll need to work with a designer to actually get it up on the internet. I have a head shot that I’ll upload, too.
Clients from the independent (private school) world - teachers, administrators
4 page

```html
<!DOCTYPE html>
<html lang="en">
<head>
<meta charset="utf-8">
<title>Bright Summit Coaching</title>
<link href="https://fonts.googleapis.com/css2?family=Cinzel:wght@400;600&family=Montserrat:wght@400;500;600;700&display=swap" rel="stylesheet">
<style>
:root{
  --teal:#17a594;
  --teal-dark:#0f8f80;
  --teal-light:#3fc4b3;
  --ink:#1c1c1c;
  --text:#3a3a3a;
  --white:#ffffff;
  --footer:#14161a;
  --field-text:#d0d0d0;
}
*{box-sizing:border-box;margin:0;padding:0}
html,body{width:1200px;height:4626px;overflow:hidden}
body{position:relative;font-family:'Montserrat',sans-serif;color:var(--text);background:var(--white)}
.abs{position:absolute}
.btn{position:absolute;display:inline-flex;align-items:center;gap:6px;background:var(--teal);color:var(--white);font-weight:700;font-size:14px;text-transform:uppercase;border-radius:22px;padding:10px 22px;box-shadow:0 0 0 3px var(--white),0 0 0 5px var(--teal)}
.btn .dot{width:13px;height:13px;border-radius:50%;background:var(--white);display:inline-block;position:relative}
.btn .dot:after{content:"";position:absolute;left:4px;top:3.5px;border-left:5px solid var(--teal);border-top:3px solid transparent;border-bottom:3px solid transparent}
.rule{position:absolute;height:3px;width:68px;background:var(--teal)}
/* nav */
.nav{position:absolute;left:0;top:0;width:1200px;height:78px;background:var(--white);z-index:3}
.nav a{position:absolute;top:33px;font-size:15px;font-weight:600;color:var(--ink);text-decoration:none}
.nav a.active{color:var(--teal)}
.brand{position:absolute;left:540px;top:8px;width:120px;height:104px;border-radius:50%;background:var(--white);display:flex;align-items:center;justify-content:center;font-size:14px;font-weight:500;color:var(--teal-dark);border:2px solid var(--teal-light);z-index:4}
/* hero */
.hero{position:absolute;left:0;top:78px;width:1200px;height:712px;background:linear-gradient(180deg,#d9dfe0 0%,#c3cccb 45%,#9aa39c 75%,#b9b0a2 100%)}
.hero h1{position:absolute;left:102px;top:205px;font-family:'Cinzel',serif;font-weight:600;font-size:47px;line-height:57px;color:var(--ink)}
.hero p{position:absolute;left:102px;top:330px;width:450px;font-size:16px;line-height:30px;color:var(--ink)}
.dots{position:absolute;left:560px;top:598px;display:flex;gap:9px}
.dots i{width:12px;height:12px;border-radius:50%;border:1.5px solid var(--white)}
.dots i.on{background:var(--white)}
/* about */
.portrait{position:absolute;left:119px;top:850px;width:460px;height:460px;border-radius:50%;background:radial-gradient(circle at 50% 45%,#e8cdb8 0 30%,#d9d6cf 55%,#b9bcbb 100%);border:6px solid var(--white);box-shadow:0 0 0 3px var(--teal)}
.copy-block{position:absolute;font-size:14.3px;line-height:30.5px;color:var(--text)}
.copy-block p+p{margin-top:7px}
.h2{position:absolute;font-family:'Cinzel',serif;font-weight:600;font-size:40px;color:var(--ink)}
/* services */
.sea{position:absolute;left:0;top:1500px;width:1200px;height:530px;background:linear-gradient(180deg,#ffffff 0%,#cfeff5 18%,#9edde6 45%,#bfe9ec 75%,#d9f2f1 100%)}
.card{position:absolute;width:236px;background:var(--white);box-shadow:0 4px 14px rgba(0,0,0,.12);text-align:center}
.card .photo{height:160px}
.card .icon{position:absolute;left:89px;top:128px;width:58px;height:58px;border-radius:50%;background:var(--teal);border:4px solid var(--white)}
.card h3{margin-top:32px;font-family:'Cinzel',serif;font-weight:600;font-size:20px;color:var(--ink)}
.card p{margin:8px auto 0;width:206px;font-size:14px;line-height:23px}
.card .more{display:inline-flex;align-items:center;gap:5px;margin:12px 0 18px;font-size:14px;font-weight:700;color:var(--teal);text-decoration:underline}
.card .more .dot{width:13px;height:13px;border-radius:50%;background:var(--teal);position:relative}
.card .more .dot:after{content:"";position:absolute;left:4px;top:3.5px;border-left:5px solid var(--white);border-top:3px solid transparent;border-bottom:3px solid transparent}
/* retreats */
.retreat-photo{position:absolute;left:0;top:2030px;width:640px;height:620px;background:radial-gradient(circle at 60% 20%,#fff3d8 0%,#e7c69a 25%,#a88d72 55%,#6f6d6c 100%)}
/* testimonials */
.testi{position:absolute;left:0;top:2600px;width:1200px;height:780px}
.quote{position:absolute;top:2912px;width:320px;height:206px;background:var(--white);border-radius:14px;text-align:center;font-style:italic;font-size:16px;line-height:33px;color:#2d2d2d;padding:52px 20px 0}
.quote:after{content:"";position:absolute;left:148px;bottom:-12px;border-top:13px solid var(--white);border-left:12px solid transparent;border-right:12px solid transparent}
.avatar{position:absolute;top:2872px;width:78px;height:78px;border-radius:50%;background:linear-gradient(160deg,#b8c9c6,#7d9894);border:3px solid var(--white);z-index:2}
.who{position:absolute;top:3145px;width:320px;text-align:center;color:var(--white)}
.who b{display:block;font-size:19px;font-weight:600}
.who small{display:block;font-size:11px;margin-top:4px}
.who .stars{color:#f2c230;font-size:17px;letter-spacing:1px;margin-top:2px}
/* blog */
.blog-photo{position:absolute;top:3531px;width:460px;height:308px}
.blog-box{position:absolute;top:3757px;width:402px;height:248px;background:var(--white);box-shadow:0 3px 12px rgba(0,0,0,.14);padding:30px 30px 0}
.date{position:absolute;left:30px;top:30px;width:42px;height:42px;border-radius:50%;background:var(--teal);color:var(--white);font-size:9px;font-weight:700;text-align:center;line-height:11px;padding-top:10px;box-shadow:0 0 0 2px var(--white),0 0 0 4px var(--teal)}
.blog-box h4{margin-left:58px;font-size:17px;font-weight:600;color:var(--ink);line-height:22px}
.blog-box p{margin-top:14px;font-size:12.5px;line-height:23px}
/* footer */
.footer{position:absolute;left:0;top:4062px;width:1200px;height:564px;background:var(--footer);color:var(--white)}
.fh{position:absolute;top:162px;font-family:'Cinzel',serif;font-size:19px;font-weight:600;color:var(--white)}
.fh:after{content:"";position:absolute;left:0;bottom:-7px;width:62px;height:2px;background:var(--white)}
.field{position:absolute;left:101px;width:375px;height:40px;border:1px solid #777;font-size:12px;padding:12px 12px;color:var(--field-text)}
.submit{position:absolute;left:101px;top:4486px;background:var(--teal);color:var(--white);font-family:'Cinzel',serif;font-size:13px;padding:6px 15px}
.contact-line{position:absolute;left:584px;font-size:15px;line-height:19px;padding-left:38px;color:var(--white)}
.contact-line .ic{position:absolute;left:0;top:2px;width:30px;height:30px;border-radius:50%;border:1.5px solid var(--white)}
.social{position:absolute;top:4466px;width:29px;height:29px;border-radius:50%;border:1.5px solid var(--white)}
.links{position:absolute;left:971px;top:4272px;font-size:15px;line-height:28px;color:var(--white)}
.copyright{position:absolute;left:0;top:4588px;width:1200px;text-align:center;font-size:14px;color:var(--white)}
</style>
</head>
<body>

<nav class="nav">
  <a class="active" style="left:101px">HOME</a>
  <a style="left:221px">ABOUT ME</a>
  <a style="left:375px">SERVICES</a>
  <a style="left:732px">TESTIMONIAL</a>
  <a style="left:906px">BLOG</a>
  <a style="left:1023px">CONTACT</a>
</nav>
<div class="brand">Bright Summit</div>

<section class="hero" role="img" aria-label="Woman in a white dress standing on a rocky shore facing the sea with arms open">
  <h1>BRIGHT SUMMIT<br>COACHING</h1>
  <p>Sed ut perspiciatis unde omnis iste natr sit voluptatem accusantium doloremque</p>
  <span class="btn" style="left:104px;top:407px">Get Started <i class="dot"></i></span>
  <svg class="abs" style="left:55px;top:310px" width="22" height="44"><path d="M20 2 L3 22 L20 42" stroke="#fff" stroke-width="2" fill="none"/></svg>
  <svg class="abs" style="left:1120px;top:310px" width="22" height="44"><path d="M2 2 L19 22 L2 42" stroke="#fff" stroke-width="2" fill="none"/></svg>
  <div class="dots"><i></i><i class="on"></i><i></i><i></i></div>
</section>
<svg class="abs" style="left:0;top:700px" width="1200" height="100" viewBox="0 0 1200 100">
  <path d="M0 100 L0 85 Q600 -30 1200 85 L1200 100 Z" fill="#fff"/>
  <path d="M0 85 Q600 -30 1200 85" stroke="#17a594" stroke-width="7" fill="none"/>
</svg>

<!-- About -->
<div class="portrait" role="img" aria-label="Head shot of the coach"></div>
<div class="h2" style="left:641px;top:862px">About Me</div>
<div class="copy-block" style="left:641px;top:940px;width:462px">
  <p>Sed ut perspiciatis unde omnis iste natus errr sit voluptatem accusantium doloremque laudantium rem aam, eaque ipsa quae ab illo invntore veritatis et quasi aro beatae vitae dicta suntcabo. Nemo enim ipstatem quia voluptas sit aspernatur aut odit aut fugit, sed quia consequuntur magni dolores eos qui ratione voluptatem sequi nesciunt.</p>
  <p>Sed ut perspiciatis unde omnis iste natus errr sit voluptatem accusantium doloremque laudantium rem aam, eaque ipsa quae ab illo invntore veritatis</p>
</div>
<span class="btn" style="left:646px;top:1250px">Learn More <i class="dot"></i></span>

<!-- Services -->
<div class="h2" style="left:0;top:1415px;width:1200px;text-align:center">Our Services</div>
<div class="rule" style="left:566px;top:1478px"></div>
<div class="sea" role="img" aria-label="Clear turquoise sea water"></div>

<div class="card" style="left:101px;top:1523px">
  <div class="photo" role="img" aria-label="Group coaching session" style="background:linear-gradient(135deg,#d8d4cf,#8a8682)"></div>
  <i class="icon"></i>
  <h3>Coaching</h3>
  <p>Sed ut perspicitis unde omnis iste natus eror sit voluptatem accusantium</p>
  <a class="more">LEARN MORE <i class="dot"></i></a>
</div>
<div class="card" style="left:355px;top:1561px">
  <div class="photo" role="img" aria-label="Woman meditating outdoors" style="background:linear-gradient(180deg,#c9b98e,#8f9c6b)"></div>
  <i class="icon"></i>
  <h3>Yoga</h3>
  <p>Sed ut perspicitis unde omnis iste natus eror sit voluptatem accusantium</p>
  <a class="more">LEARN MORE <i class="dot"></i></a>
</div>
<div class="card" style="left:609px;top:1523px">
  <div class="photo" role="img" aria-label="Relaxing massage treatment" style="background:linear-gradient(135deg,#6b5646,#d6c3b0)"></div>
  <i class="icon"></i>
  <h3>Massage</h3>
  <p>Sed ut perspicitis unde omnis iste natus eror sit voluptatem accusantium</p>
  <a class="more">LEARN MORE <i class="dot"></i></a>
</div>
<div class="card" style="left:864px;top:1561px">
  <div class="photo" role="img" aria-label="Woman eating a fresh salad" style="background:linear-gradient(135deg,#c98a4f,#e9d8b8)"></div>
  <i class="icon"></i>
  <h3>Healthy Food</h3>
  <p>Sed ut perspicitis unde omnis iste natus eror sit voluptatem accusantium</p>
  <a class="more">LEARN MORE <i class="dot"></i></a>
</div>

<!-- Retreats -->
<div class="retreat-photo" role="img" aria-label="Stacked stones labelled spirit, soul, mind and body at sunset"></div>
<div class="h2" style="left:638px;top:2110px">Retreats</div>
<div class="copy-block" style="left:636px;top:2184px;width:466px">
  <p>Sed ut perspiciatis unde omnis iste natus errr sit voluptatem accusantium doloremque laudantium rem aam, eaque ipsa quae ab illo invntore veritatis et quasi aro beatae vitae dicta suntcabo. Nemo enim ipstatem quia voluptas sit aspernatur aut odit aut fugit, sed quia consequuntur magni dolores eos qui ratione voluptatem sequi nesciunt.</p>
  <p>Sed ut perspiciatis unde omnis iste natus errr sit voluptatem accusantium doloremque laudantium rem aam, eaque ipsa quae ab illo invntore veritatis</p>
</div>
<span class="btn" style="left:641px;top:2494px">Learn More <i class="dot"></i></span>

<!-- Testimonials -->
<svg class="testi" viewBox="0 0 1200 780" preserveAspectRatio="none" role="img" aria-label="Teal band with a misty mountain scene">
  <defs><linearGradient id="tg" x1="0" y1="0" x2="0" y2="1"><stop offset="0" stop-color="#25b9a7"/><stop offset="1" stop-color="#1aa493"/></linearGradient></defs>
  <path d="M0 40 Q300 90 600 40 T1200 20 L1200 720 Q900 650 600 720 T0 720 Z" fill="url(#tg)"/>
  <path d="M0 720 Q300 770 600 720 T1200 700" stroke="#6fd7ca" stroke-width="6" fill="none"/>
</svg>
<div class="h2" style="left:0;top:2762px;width:1200px;text-align:center;color:#fff">Testimonials</div>
<div class="rule" style="left:566px;top:2822px;background:#fff"></div>

<div class="avatar" style="left:221px"></div>
<div class="quote" style="left:101px">At vero eos et accusaus et iusto odio diismos duus qui blanditiis pesentium voluptatum deleniti atque corrupti</div>
<div class="who" style="left:101px"><b>- Maya Collins</b><small>Finibus Bonorum</small><div class="stars">★★★★★</div></div>

<div class="avatar" style="left:561px"></div>
<div class="quote" style="left:441px">At vero eos et accusaus et iusto odio diismos duus qui blanditiis pesentium voluptatum deleniti atque corrupti</div>
<div class="who" style="left:441px"><b>- Maya Collins</b><small>Finibus Bonorum</small><div class="stars">★★★★★</div></div>

<div class="avatar" style="left:900px"></div>
<div class="quote" style="left:780px">At vero eos et accusaus et iusto odio diismos duus qui blanditiis pesentium voluptatum deleniti atque corrupti</div>
<div class="who" style="left:780px"><b>- Maya Collins</b><small>Finibus Bonorum</small><div class="stars">★★★★★</div></div>

<!-- Blog -->
<div class="h2" style="left:0;top:3425px;width:1200px;text-align:center">Latest Blog</div>
<div class="rule" style="left:566px;top:3487px"></div>

<div class="blog-photo" style="left:120px;background:linear-gradient(90deg,#d9b8a0,#f1ece6 50%,#c99b83)" role="img" aria-label="Two women talking in a bright room"></div>
<div class="blog-box" style="left:149px">
  <span class="date">OCT<br>2022</span>
  <h4>NEMO ENIM IPSAM VOLUPTA QUIA VOLUPTAS SIT</h4>
  <p>Sed ut perspiciatis unde omnis iste natus evoluptatem accusantium doloremque laudantium, m rem aperiam, eaque ipsa quae ab illo inntore veritatis uasi architecto beatae vitae</p>
  <span class="btn" style="left:35px;top:198px">Learn More <i class="dot"></i></span>
</div>

<div class="blog-photo" style="left:621px;background:linear-gradient(180deg,#c9c6c6,#9c8e88 60%,#6e5b55)" role="img" aria-label="Woman sitting on a hilltop looking at the view"></div>
<div class="blog-box" style="left:649px">
  <span class="date">OCT<br>2022</span>
  <h4>NEMO ENIM IPSAM VOLUPTA QUIA VOLUPTAS SIT</h4>
  <p>Sed ut perspiciatis unde omnis iste natus evoluptatem accusantium doloremque laudantium, m rem aperiam, eaque ipsa quae ab illo inntore veritatis uasi architecto beatae vitae</p>
  <span class="btn" style="left:35px;top:198px">Learn More <i class="dot"></i></span>
</div>

<!-- Footer -->
<footer class="footer" role="img" aria-label="Dark mountain silhouette background">
  <svg class="abs" style="left:0;top:-2px" width="1200" height="90" viewBox="0 0 1200 90">
    <path d="M0 0 L1200 0 L1200 20 Q600 120 0 20 Z" fill="#fff"/>
    <path d="M0 20 Q600 120 1200 20" stroke="#17a594" stroke-width="6" fill="none"/>
  </svg>
  <div class="fh" style="left:101px">Book a Consultation</div>
  <div class="fh" style="left:584px">Contact Us</div>
  <div class="fh" style="left:971px">Qucik Links</div>
</footer>
<div class="field" style="top:4270px">First Name</div>
<div class="field" style="top:4320px">Email Address</div>
<div class="field" style="top:4369px">Phone Number</div>
<div class="field" style="top:4419px;height:62px">Message</div>
<div class="submit">SUBMIT</div>

<div class="contact-line" style="top:4275px"><i class="ic"></i>48 Larkfield Lane Easton<br>USA 20416</div>
<div class="contact-line" style="top:4336px"><i class="ic"></i>Phone:<br>+1 555-010-2040</div>
<div class="contact-line" style="top:4397px"><i class="ic"></i>Email:<br>hello@brightsummit.example</div>
<i class="social" style="left:584px"></i>
<i class="social" style="left:622px"></i>
<i class="social" style="left:660px"></i>
<i class="social" style="left:698px"></i>

<div class="links">Home<br>About Us<br>Services<br>Testimonial<br>Faq<br>Blog<br>Contact</div>
<div class="abs" style="left:101px;top:4560px;width:999px;height:1px;background:#555"></div>
<div class="copyright">©Copyright ©2022 Bright Summit. All Rights Reserved.</div>

</body>
</html>
```